Velis Tarn

We are an online company, specialising in Relationship enhancement & sexual health. Empowering couples & singles to learn more about their bodies & enhance their sex lives.

We are looking to create a flyer to hand to customers & mail out. We want to peak their interest to bring them to our website.

I want to stress that we want a professional, elegant message, keeping away from the usual innuendos of adult stores.

Something suggestive, but not corny.

Visit our Website www.velistarn.com.au to get a feel of our business.

Target Market(s)

Women 16+
Couples of all ages

Industry/Entity Type

It Company

Font styles to use
Serif

Requirements
Must have
• Logo
• Website URL - www.velistarn.com.au
• Logo of Facebook, instagram
• Our slogan 'Elevate your life'
Nice to have
• Discount offered
Should not have
• Sleezy
• No nudity

```html
<!DOCTYPE html>
<html lang="en">
<head>
<meta charset="utf-8">
<title>Velis Tarn — Elevate your life</title>
<link rel="stylesheet" href="https://fonts.googleapis.com/css2?family=Cormorant+SC:wght@600&family=Open+Sans:wght@400;600&display=swap">
<style>
  :root {
    --ink: #111111;
    --paper: #ffffff;
    --red-deep: #8e0208;
    --red-mid: #c40d14;
    --red-glow: #ef3a3a;
    --heart-shade: #7a0006;
    --rule: rgba(255,255,255,0.85);
    --footer-text: #333333;
    --social: #3b5998;
    --social-alt: #6b4a3a;
  }
  * { margin: 0; padding: 0; box-sizing: border-box; }
  html, body { width: 1200px; height: 2212px; overflow: hidden; background: var(--paper); }
  .flyer {
    position: relative;
    width: 1200px;
    height: 2212px;
    background: var(--paper);
    overflow: hidden;
  }
  .top-band {
    position: absolute; left: 0; top: 0; width: 1200px; height: 30px;
    background: var(--ink);
  }
  .brand {
    position: absolute; left: 0; top: 140px; width: 1200px;
    display: flex; align-items: center; justify-content: center; gap: 28px;
  }
  .brand-dot {
    width: 90px; height: 90px; border-radius: 50%;
    background: var(--ink);
  }
  .brand-name {
    font-family: "Open Sans", sans-serif;
    font-weight: 600;
    font-size: 84px;
    letter-spacing: 1px;
    color: var(--ink);
  }
  .red-field {
    position: absolute; left: 0; top: 380px; width: 1200px; height: 1680px;
    background: radial-gradient(ellipse 70% 55% at 50% 55%, var(--red-glow) 0%, var(--red-mid) 45%, var(--red-deep) 100%);
  }
  .heart {
    position: absolute; left: 0; top: 360px; width: 1200px; height: 1200px;
  }
  .slogan {
    position: absolute; left: 0; top: 1495px; width: 1200px;
    text-align: center;
    font-family: "Cormorant SC", serif;
    font-weight: 600;
    font-size: 104px;
    line-height: 120px;
    color: var(--ink);
    letter-spacing: 1px;
  }
  .intro {
    position: absolute; left: 90px; top: 1625px; width: 1020px;
    text-align: center;
    font-family: "Open Sans", sans-serif;
    font-size: 36px;
    line-height: 42px;
    color: var(--paper);
  }
  .rule {
    position: absolute; left: 60px; width: 1080px; height: 3px;
    background: var(--rule);
  }
  .rule-upper { top: 1800px; }
  .rule-lower { top: 2005px; }
  .offer {
    position: absolute; left: 150px; top: 1815px; width: 900px;
    text-align: center;
    font-family: "Open Sans", sans-serif;
    font-size: 50px;
    line-height: 58px;
    color: var(--paper);
    text-transform: uppercase;
  }
  .footer {
    position: absolute; left: 0; top: 2060px; width: 1200px; height: 152px;
    display: flex; align-items: center; justify-content: space-between;
    padding: 0 150px 0 230px;
  }
  .site-url {
    font-family: "Open Sans", sans-serif;
    font-size: 44px;
    color: var(--footer-text);
  }
  .social { display: flex; gap: 20px; }
  .social-square {
    width: 64px; height: 64px; border-radius: 8px;
    background: var(--social);
  }
  .social-square.alt { background: var(--social-alt); }
</style>
</head>
<body>
<main class="flyer">
  <div class="top-band"></div>

  <header class="brand">
    <span class="brand-dot"></span>
    <span class="brand-name">Velis Tarn</span>
  </header>

  <section class="red-field"></section>

  <svg class="heart" viewBox="0 0 1200 1200">
    <defs>
      <linearGradient id="heart-photo-tone" x1="0" y1="0" x2="0.3" y2="1">
        <stop offset="0" stop-color="#d9d2cc"/>
        <stop offset="0.45" stop-color="#b98c78"/>
        <stop offset="1" stop-color="#5a3a34"/>
      </linearGradient>
    </defs>
    <path d="M600 190 C 520 40, 250 -20, 100 100 C -40 220, 10 470, 160 660 C 310 850, 520 1010, 600 1150 C 680 1010, 890 850, 1040 660 C 1190 470, 1240 220, 1100 100 C 950 -20, 680 40, 600 190 Z"
          fill="var(--heart-shade)" opacity="0.55"/>
    <path d="M600 210 C 525 75, 270 20, 135 130 C 10 235, 55 460, 190 635 C 330 815, 525 965, 600 1095 C 675 965, 870 815, 1010 635 C 1145 460, 1190 235, 1065 130 C 930 20, 675 75, 600 210 Z"
          fill="url(#heart-photo-tone)" stroke="var(--paper)" stroke-width="16"
          role="img" aria-label="Photograph of a couple embracing in soft light, with a bottle of lubricant and a pink personal massager in its box in the foreground"/>
  </svg>

  <h1 class="slogan">Elevate your life</h1>

  <p class="intro">We are an online company, specialising in Relationship enhancement &amp; sexual health. Empowering couples &amp; singles to learn more about their bodies &amp; enhance their sex lives.</p>

  <div class="rule rule-upper"></div>
  <p class="offer">Enter your details for your chance to win a mystery gift valued at $150!</p>
  <div class="rule rule-lower"></div>

  <footer class="footer">
    <span class="site-url">www.velistarn.com.au</span>
    <div class="social">
      <span class="social-square" aria-label="Social page"></span>
      <span class="social-square alt" aria-label="Photo page"></span>
    </div>
  </footer>
</main>
</body>
</html>
```